Brightwire Hollow Business cards

one side I would like my logo (uploaded) and the other side I want my details. I'm an electrician in sydney. The logo side I'm happy with just a white background and our logo in the middle.

Details for other side
24/7 Sydney Electrician
Marcus Pell
0431 587 219
marcus@brightwirehollow.com.au
brightwirehollow.com.au
icons for facebook, instagram, linked in

Industry/Entity Type

electrician

Contact Information for Business Card

company info

```html
<!DOCTYPE html>
<html lang="en">
<head>
<meta charset="utf-8">
<title>Brightwire Hollow – Business Cards</title>
<link rel="stylesheet" href="https://fonts.googleapis.com/css2?family=Michroma&family=Source+Sans+3:wght@400;600&display=swap">
<style>
  :root {
    --bg: #1c1c1c;
    --card: #0b0b0b;
    --red: #ee3524;
    --white: #ffffff;
    --rule: #555555;
  }
  * { box-sizing: border-box; margin: 0; padding: 0; }
  html, body { width: 1200px; height: 900px; overflow: hidden; }
  body {
    background: var(--bg);
    font-family: "Source Sans 3", sans-serif;
    display: flex;
    align-items: center;
    justify-content: center;
    gap: 40px;
  }
  .card {
    position: relative;
    width: 540px;
    height: 330px;
    background: var(--card);
    border-radius: 22px;
    overflow: hidden;
    box-shadow: 0 14px 30px rgba(0,0,0,.5);
  }
  .card__band {
    position: absolute;
    left: 0; right: 0; bottom: 0;
    height: 74px;
    background: var(--red);
    display: flex;
    align-items: center;
    justify-content: center;
  }
  .tagline {
    color: var(--white);
    font-size: 19px;
    letter-spacing: 1px;
    text-transform: uppercase;
  }
  .brand-name {
    color: var(--red);
    font-family: "Source Sans 3", sans-serif;
    font-weight: 600;
    text-transform: uppercase;
    line-height: 1.05;
  }

  /* Details side */
  .details__brand {
    position: absolute;
    left: 34px; top: 88px;
    width: 200px;
    font-size: 30px;
    letter-spacing: 2px;
  }
  .details__rule {
    position: absolute;
    left: 252px; top: 62px;
    width: 1px; height: 150px;
    background: var(--rule);
  }
  .details__info {
    position: absolute;
    left: 276px; top: 60px;
  }
  .person {
    font-family: "Michroma", sans-serif;
    color: var(--red);
    font-size: 19px;
    letter-spacing: 1px;
    text-transform: uppercase;
    margin-bottom: 20px;
  }
  .contact { list-style: none; }
  .contact__item {
    display: flex;
    align-items: center;
    gap: 10px;
    color: var(--white);
    font-size: 15px;
    margin-bottom: 9px;
  }
  .contact__icon { width: 20px; height: 20px; flex: none; }

  /* Logo side */
  .brand-side__name {
    position: absolute;
    left: 0; right: 0; top: 100px;
    text-align: center;
    font-size: 40px;
    letter-spacing: 4px;
  }
  .social {
    position: absolute;
    left: 0; right: 0; top: 222px;
    display: flex;
    justify-content: center;
    gap: 6px;
  }
  .social__dot {
    width: 18px; height: 18px;
    border: 1.5px solid var(--white);
    border-radius: 50%;
  }
</style>
</head>
<body>

  <section class="card card--details">
    <div class="brand-name details__brand">Brightwire<br>Hollow</div>
    <div class="details__rule"></div>
    <div class="details__info">
      <h1 class="person">Marcus Pell</h1>
      <ul class="contact">
        <li class="contact__item">
          <svg class="contact__icon" viewBox="0 0 20 20" aria-hidden="true">
            <circle cx="10" cy="10" r="9" fill="none" stroke="#ee3524" stroke-width="1.3"/>
            <path d="M7 5.5l1.6 2.2-1 1.1c.6 1.3 1.5 2.2 2.7 2.8l1.1-1 2.1 1.6-.9 1.6c-3.4-.3-6.3-3.3-6.6-6.7z" fill="#ee3524"/>
          </svg>
          0431 587 219
        </li>
        <li class="contact__item">
          <svg class="contact__icon" viewBox="0 0 20 20" aria-hidden="true">
            <circle cx="10" cy="10" r="9" fill="none" stroke="#ee3524" stroke-width="1.3"/>
            <rect x="5.5" y="7" width="9" height="6.5" fill="none" stroke="#ee3524" stroke-width="1.2"/>
            <path d="M5.5 7l4.5 3.5L14.5 7" fill="none" stroke="#ee3524" stroke-width="1.2"/>
          </svg>
          marcus@brightwirehollow.com.au
        </li>
        <li class="contact__item">
          <svg class="contact__icon" viewBox="0 0 20 20" aria-hidden="true">
            <circle cx="10" cy="10" r="9" fill="none" stroke="#ee3524" stroke-width="1.3"/>
            <circle cx="10" cy="10" r="5" fill="none" stroke="#ee3524" stroke-width="1.1"/>
            <ellipse cx="10" cy="10" rx="2.2" ry="5" fill="none" stroke="#ee3524" stroke-width="1"/>
            <path d="M5 10h10" stroke="#ee3524" stroke-width="1"/>
          </svg>
          brightwirehollow.com.au
        </li>
      </ul>
    </div>
    <div class="card__band"><span class="tagline">24/7 Sydney Electrician</span></div>
  </section>

  <section class="card card--brand">
    <div class="brand-name brand-side__name">Brightwire<br>Hollow</div>
    <div class="social" aria-label="Social profiles">
      <span class="social__dot"></span>
      <span class="social__dot"></span>
      <span class="social__dot"></span>
    </div>
    <div class="card__band"></div>
  </section>

</body>
</html>
```